KM Group

We need a new website for our company and since we had a very good work done for our logo in this site, we're back for the entire job.

Our company name is Halvorsen Capital Group. We're adding files of examples of what we have done today. In my opinion we need a more attention lock in the site but yet financial simple work.

Our files (attached) will let you know what we have so far. We need a complete change but the colours should be the same, however you can change them not running away to far from the original, and of course matching with the logo.

We need examples for 3 kind of layouts.

- A HOME welcome layout
- An internal Layout with sidebar
- And internal Layout wide

We can buy image licenses if needed for assets.
Actually there are 5 slide images placed on the Welcome HOME, we need those there, but you can improve with better images to match the new website!!!

Target Market(s)

Clients looking for financial advisers, tax and funds specialist, currency advisers

Industry/Entity Type

Financial

Requirements
Must have
• all the fonts must be in accordance with the financial market sites........the welcome home page must be precise, neat and information accurate........the menu should be elegant........main focus on the Home page, should be also the PRIVATE ACCESS box log in.......

```html
<!DOCTYPE html>
<html lang="en">
<head>
<meta charset="utf-8">
<title>Halvorsen Capital Group</title>
<link rel="stylesheet" href="https://fonts.googleapis.com/css2?family=PT+Sans+Narrow:wght@400;700&family=Arimo:wght@400;700&display=swap">
<style>
:root{
  --orange:#f07b22;
  --orange-dark:#d9661a;
  --nav:#1c1c1e;
  --nav-line:#3a3a3c;
  --footer:#0d0d0f;
  --header-bg:#e6e9ef;
  --panel:#d6e0ec;
  --ink:#222;
  --muted:#9a9a9a;
  --link:#3a8fd8;
  --white:#fff;
}
*{box-sizing:border-box;margin:0;padding:0}
html,body{width:980px;height:1200px;overflow:hidden;background:var(--white)}
body{position:relative;font-family:"Arimo",Arial,sans-serif;color:var(--ink)}
.abs{position:absolute}

/* header */
.site-header{left:0;top:0;width:980px;height:116px;background:var(--header-bg)}
.brand{left:68px;top:30px;display:flex;align-items:center;gap:10px}
.brand-mark{width:30px;height:30px;background:var(--orange)}
.brand-name{font-family:"PT Sans Narrow",sans-serif;font-size:19px;color:#2b2b2b;letter-spacing:.5px}
.utility{right:74px;top:68px;display:flex;align-items:center;gap:14px;font-family:"PT Sans Narrow",sans-serif;font-size:17px;color:#6a6a6a}
.utility span{display:flex;align-items:center;gap:6px}
.utility .sep{color:#999}

/* nav */
.main-nav{left:0;top:116px;width:980px;height:59px;background:var(--nav)}
.nav-item{top:116px;height:59px;line-height:59px;font-family:"PT Sans Narrow",sans-serif;font-size:18px;color:var(--white);z-index:2}
.nav-sep{top:140px;width:1px;height:13px;background:var(--nav-line);z-index:2}
.nav-active{left:174px;top:116px;width:70px;height:59px;background:var(--orange)}

/* dropdown */
.dropdown{left:174px;top:182px;width:148px;z-index:3}
.dropdown div{height:21px;line-height:21px;padding-left:18px;font-family:"PT Sans Narrow",sans-serif;font-size:16px;color:var(--white);background:rgba(20,20,22,.9);border-bottom:1px solid #555}
.dropdown .on{background:var(--orange);position:relative}
.submenu{left:324px;top:204px;width:149px;z-index:3}
.submenu div{height:20px;line-height:20px;padding-left:18px;font-family:"PT Sans Narrow",sans-serif;font-size:16px;color:var(--white);background:rgba(20,20,22,.9);border-bottom:1px solid #555}

/* hero */
.hero-photo{left:68px;top:182px;width:622px;height:255px;background:linear-gradient(135deg,#d8dde4 0%,#9aa4b2 40%,#2a3346 70%,#dfe3e9 100%)}
.hero-caption{left:60px;top:299px;width:557px;height:91px;background:rgba(12,12,14,.85);padding:10px 22px}
.hero-caption h2{font-family:"PT Sans Narrow",sans-serif;font-weight:400;font-size:22px;color:var(--orange)}
.hero-caption p{font-family:"PT Sans Narrow",sans-serif;font-size:16.5px;line-height:20px;color:var(--white);margin-top:2px}
.slider-dots{left:635px;top:446px;display:flex;gap:3px}
.slider-dots i{width:9px;height:9px;border-radius:50%;border:1px solid #777;background:var(--white)}
.slider-dots i.on{background:var(--orange);border-color:var(--orange)}

/* private access */
.private-access{left:695px;top:182px;width:211px;height:255px;background:var(--orange);padding:14px 10px}
.private-access h3{font-family:"PT Sans Narrow",sans-serif;font-weight:400;font-size:23px;color:var(--white)}
.pa-icon{left:165px;top:8px;width:38px;height:38px;border-radius:50%;background:#f79a4e;border:2px solid #fbb57c}
.pa-field{left:8px;width:194px;height:26px;background:#f2ece6;font-size:11px;color:#aaa;padding:7px 8px}
.pa-forgot{left:10px;top:138px;font-size:11px;color:var(--white)}
.pa-login{left:8px;top:180px;width:86px;height:28px;background:#111;color:var(--white);font-size:12px;text-align:center;line-height:28px}

/* feature panel */
.features{left:68px;top:469px;width:839px;height:265px;background:var(--panel)}
.feature{top:486px;width:238px}
.feature h4{font-family:"PT Sans Narrow",sans-serif;font-weight:400;font-size:19px;color:#1a1a1a}
.feature-img{width:238px;height:102px;margin-top:14px;box-shadow:0 3px 6px rgba(0,0,0,.25)}
.feature p{margin-top:12px;font-size:11px;line-height:13.5px;color:#333;letter-spacing:.2px}
.feature .more{font-size:10px;color:var(--link);margin-top:2px}
.feature-divider{top:489px;width:1px;height:232px;background:#b9c6d4}

/* partners */
.partners-title{left:68px;top:748px;font-family:"PT Sans Narrow",sans-serif;font-weight:400;font-size:18px;color:#1a1a1a}
.partners{left:68px;top:776px;width:839px;height:47px;background:#f3f3f3}
.partner{top:9px;height:28px;background:#cfcfcf;border-radius:4px}
.partner.round{border-radius:50%;width:30px}
.ticker{left:68px;top:845px;width:839px;height:29px;border:1px solid #ddd;background:#f9f9f9;font-size:10.5px;font-weight:700;line-height:27px;padding-left:14px;white-space:nowrap;overflow:hidden;color:#222}
.ticker .up{color:#2a9a2a}
.ticker .down{color:#d22}
.ticker .flat{color:#f0a020}
.ticker span{margin-right:18px}

/* footer */
.site-footer{left:0;top:890px;width:980px;height:270px;background:var(--footer)}
.f-col{top:912px}
.f-col h5{font-family:"PT Sans Narrow",sans-serif;font-weight:400;font-size:18.5px;color:var(--white);margin-bottom:5px}
.f-col li{list-style:none;font-family:"PT Sans Narrow",sans-serif;font-size:13.5px;line-height:21.5px;color:var(--muted)}
.verified{left:740px;top:1043px;width:161px;height:80px;background:#e9f2e5;border-radius:6px}
.badge{background:#b8c4cc;border-radius:3px}
.copyright{left:0;top:1140px;width:980px;text-align:center;font-size:10px;color:#ddd}
</style>
</head>
<body>

<header class="site-header abs"></header>
<div class="brand abs">
  <div class="brand-mark"></div>
  <div class="brand-name">Halvorsen Capital Group</div>
</div>
<div class="utility abs">
  <span>
    <svg width="20" height="16" viewBox="0 0 20 16"><rect x="1" y="3" width="13" height="12" fill="none" stroke="#555" stroke-width="1.5"/><path d="M8 10 L18 1" stroke="#555" stroke-width="2"/></svg>
    Apply Now
  </span>
  <span class="sep">|</span>
  <span>
    <svg width="20" height="14" viewBox="0 0 20 14"><path d="M1 5 Q10 -2 19 5 L16 7 L14 4 L6 4 L4 7 Z" fill="#555"/><rect x="4" y="7" width="12" height="6" rx="1" fill="#555"/></svg>
    Contact Us
  </span>
</div>

<nav class="main-nav abs"></nav>
<div class="nav-active abs"></div>
<svg class="abs" style="left:203px;top:163px;z-index:2" width="12" height="7"><path d="M0 0 L12 0 L6 6 Z" fill="#fff"/></svg>
<div class="nav-item abs" style="left:82px">Home</div>
<div class="nav-sep abs" style="left:159px"></div>
<div class="nav-item abs" style="left:184px">About us</div>
<div class="nav-sep abs" style="left:273px"></div>
<div class="nav-item abs" style="left:309px">Investments</div>
<div class="nav-sep abs" style="left:410px"></div>
<div class="nav-item abs" style="left:448px">Funds</div>
<div class="nav-sep abs" style="left:517px"></div>
<div class="nav-item abs" style="left:552px">Brokerage</div>
<div class="nav-sep abs" style="left:640px"></div>
<div class="nav-item abs" style="left:677px">Exchange</div>
<div class="nav-sep abs" style="left:760px"></div>
<div class="nav-item abs" style="left:799px">Accounts</div>
<div class="nav-sep abs" style="left:877px"></div>

<div class="hero-photo abs" role="img" aria-label="Photo of bankers in suits working together at a desk with documents"></div>

<div class="dropdown abs">
  <div>History</div>
  <div class="on">Expertize<svg style="position:absolute;right:12px;top:6px" width="6" height="9"><path d="M0 0 L6 4.5 L0 9 Z" fill="#fff"/></svg></div>
  <div>Identity</div>
  <div>Strategy</div>
</div>
<div class="submenu abs">
  <div>Lorem ipsum dolor</div>
  <div>Lorem ipsum</div>
  <div>Lorem ipsum dolor</div>
</div>

<div class="hero-caption abs">
  <h2>Teamwork for your benefit</h2>
  <p>Our dedicated Private Bankers, will proactively keep you up to date with relevant information and providea financial overview that enables you to make better decisions.</p>
</div>
<div class="slider-dots abs"><i class="on"></i><i></i><i></i><i></i><i></i></div>

<section class="private-access abs">
  <h3>Private Access</h3>
  <div class="pa-icon abs"></div>
  <div class="pa-field abs" style="top:68px">Acc. Number</div>
  <div class="pa-field abs" style="top:102px">Acc. password</div>
  <div class="pa-forgot abs">Forget Password?</div>
  <div class="pa-login abs">LOGIN</div>
</section>

<section class="features abs"></section>
<div class="feature-divider abs" style="left:344px"></div>
<div class="feature-divider abs" style="left:618px"></div>

<article class="feature abs" style="left:88px">
  <h4>Management &amp; Strategy</h4>
  <div class="feature-img" role="img" aria-label="Photo of a hand with a pen over financial charts" style="background:linear-gradient(135deg,#f4f4f4,#c9d3dc 60%,#7fb0d0)"></div>
  <p>Lorem ipsum dolor sit amet, consectetur adip-isicing elit, sed do eiusmod tempor incididunt ut labore et dolore magna aliqua. Ut enim ad minim veniam, quis nostrud exercitation ullam-co laboris nisi ut aliquip ex ea commodo</p>
  <div class="more">more ▸</div>
</article>
<article class="feature abs" style="left:359px">
  <h4>Funds</h4>
  <div class="feature-img" role="img" aria-label="Illustration of golden currency symbols" style="background:linear-gradient(135deg,#f7e3a0,#d9a22c 55%,#8a5a10)"></div>
  <p>Lorem ipsum dolor sit amet, consectetur adip-isicing elit, sed do eiusmod tempor incididunt ut labore et dolore magna aliqua. Ut enim ad minim veniam, quis nostrud exercitation ullam-co laboris nisi ut aliquip ex ea commodo</p>
  <div class="more">more ▸</div>
</article>
<article class="feature abs" style="left:636px">
  <h4>Currency Exchange</h4>
  <div class="feature-img" role="img" aria-label="Photo of glass office towers behind palm trees" style="background:linear-gradient(180deg,#6fa8d8,#a9c7e0 50%,#2f5e3a)"></div>
  <p>Lorem ipsum dolor sit amet, consectetur adip-isicing elit, sed do eiusmod tempor incididunt ut labore et dolore magna aliqua. Ut enim ad minim veniam, quis nostrud exercitation ullam-co laboris nisi ut aliquip ex ea commodo</p>
  <div class="more">more ▸</div>
</article>

<h3 class="partners-title abs">Our Partners</h3>
<section class="partners abs">
  <svg class="abs" style="left:-6px;top:16px" width="8" height="14"><path d="M7 1 L1 7 L7 13" stroke="#222" stroke-width="2" fill="none"/></svg>
  <div class="partner abs" style="left:14px;width:56px"></div>
  <div class="partner round abs" style="left:92px"></div>
  <div class="partner abs" style="left:178px;width:74px"></div>
  <div class="partner round abs" style="left:278px"></div>
  <div class="partner abs" style="left:334px;width:56px"></div>
  <div class="partner abs" style="left:406px;width:80px"></div>
  <div class="partner abs" style="left:520px;width:56px"></div>
  <div class="partner round abs" style="left:600px"></div>
  <div class="partner abs" style="left:686px;width:74px"></div>
  <div class="partner round abs" style="left:788px"></div>
  <svg class="abs" style="left:830px;top:16px" width="8" height="14"><path d="M1 1 L7 7 L1 13" stroke="#222" stroke-width="2" fill="none"/></svg>
</section>

<div class="ticker abs">
  <span class="up">▲</span>
  <span>GBP/UAH = <b class="up">12.65761 ▲</b></span>
  <span>GBP/UGX = <b class="down">4010.06174 ▼</b></span>
  <span>GBP/USD = <b class="up">1.55817 ▲</b></span>
  <span>GBP/UYU = <b class="up">34.36026 ▲</b></span>
  <span>GBP/VEF = <b class="flat">0</b></span>
  <span>GBP/VUV = <b class="up">151.7</b></span>
</div>

<footer class="site-footer abs"></footer>
<div class="f-col abs" style="left:70px"><h5>About Us</h5><ul><li>History</li><li>Expertize</li><li>Identity</li><li>Strategy</li><li>Contact Us</li></ul></div>
<div class="f-col abs" style="left:198px"><h5>Investements</h5><ul><li>Term Deposits</li><li>Management &amp; Strategy</li><li>Client Relations</li><li>Financial Privacy</li><li>Tax Advice</li><li>Welth Analysis &amp; Financial Planning</li><li>Active Advisory Group</li><li>Manager Selection Services</li><li>Private Equity</li></ul></div>
<div class="f-col abs" style="left:408px"><h5>Funds</h5><ul><li>Overview</li><li>Administration</li><li>Funds Security</li><li>Core Services</li><li>Reporting</li><li>Revenue Opportunities</li><li>How it works?</li><li>Glossary</li></ul></div>
<div class="f-col abs" style="left:565px"><h5>Currency Exchange</h5><ul><li>Foreign Exchange</li><li>Fx Forward</li><li>Fx Options</li></ul></div>
<div class="f-col abs" style="left:565px;top:1018px"><h5>Accounts</h5><ul><li>Apply Now</li><li>Private Access</li></ul></div>
<div class="f-col abs" style="left:738px"><h5>Brokerage</h5><ul><li>Institutional</li><li>Research</li><li>Trading</li></ul></div>
<div class="f-col abs" style="left:738px;top:1010px"><h5>Verified and Protected by</h5></div>
<div class="verified abs">
  <div class="badge abs" style="left:12px;top:10px;width:62px;height:24px"></div>
  <div class="badge abs" style="left:92px;top:6px;width:30px;height:30px;border-radius:50%"></div>
  <div class="badge abs" style="left:10px;top:46px;width:80px;height:20px"></div>
  <div class="badge abs" style="left:118px;top:42px;width:30px;height:30px;border-radius:50%"></div>
</div>
<div class="copyright abs">© Copyright 2013 Halvorsen Capital Group - All rights reserved.</div>

</body>
</html>
```